Corporate Branding - Web and Print

A UK based company will like to use an existing logo to create branding materials for all marketing related documents, including business card, prints, letterhead, Website, Twitter, Facebook, Instagram logo etc. This company serves high-end clientele in the fashion, health and wellness and as such high quality and class is of utmost importance.
Where the logo can be modernised without losing its character then experiment. The main thing is to have a corporate branding which can be used later for brochures, Business Plan infographics.
The prominent colour within the organisation is burnt orange with no secondary colour. However if you believe a secondary colour is needed then use it, otherwise keep it simple and classy. Any chosen colours have to match perfectly.
Target Market(s)
High net worth individuals
Industry/Entity Type
Health And Wellness
Contact Information for Business Card
classy
Look and feel
Each slider illustrates characteristics of the customer's brand and the style your logo design should communicate.

```html
<!DOCTYPE html>
<html lang="en">
<head>
<meta charset="UTF-8">
<title>Velmora Business Card</title>
<link rel="stylesheet" href="https://fonts.googleapis.com/css2?family=Open+Sans:wght@400;600;700;800&display=swap">
<style>
  :root {
    --backdrop: #2b2b2d;
    --card: #121213;
    --card-edge: #1c1c1e;
    --orange: #f7941d;
    --text-light: #e6e6e6;
    --text-soft: #c9c9c9;
  }
  * { margin: 0; padding: 0; box-sizing: border-box; }
  html, body {
    width: 1200px; height: 900px; overflow: hidden;
    background: var(--backdrop);
    font-family: "Open Sans", Arial, sans-serif;
  }
  .stage {
    position: relative; width: 1200px; height: 900px;
    display: flex; align-items: center; justify-content: center; gap: 40px;
  }
  .card {
    width: 525px; height: 300px;
    background: var(--card);
    border-radius: 20px;
    box-shadow: 0 0 0 1px var(--card-edge);
    position: relative;
  }
  .card-front { display: flex; align-items: center; }
  .front-brand {
    width: 255px; height: 100%;
    display: flex; align-items: center; justify-content: center; gap: 12px;
  }
  .brand-dot {
    width: 34px; height: 34px; border-radius: 50%;
    background: var(--orange);
  }
  .brand-name {
    color: var(--orange);
    font-weight: 800; font-size: 30px; letter-spacing: 1px;
  }
  .front-details { flex: 1; padding-right: 30px; }
  .person-name {
    color: var(--orange); font-weight: 700; font-size: 19px; line-height: 1.1;
  }
  .person-title {
    color: var(--text-light); font-size: 13px; margin-bottom: 18px;
  }
  .address {
    color: var(--text-light); font-size: 13px; line-height: 1.35; margin-bottom: 14px;
  }
  .contact-list { list-style: none; }
  .contact-list li {
    display: flex; align-items: center; gap: 10px;
    color: var(--text-light); font-size: 13px; line-height: 1.6;
  }
  .contact-icon { width: 11px; height: 11px; flex: none; }
  .contact-icon * { fill: var(--orange); }
  .card-back {
    display: flex; align-items: center; justify-content: center; gap: 14px;
  }
  .card-back .brand-dot { width: 44px; height: 44px; }
  .card-back .brand-name { font-size: 44px; }
</style>
</head>
<body>
<main class="stage">
  <section class="card card-front">
    <div class="front-brand">
      <span class="brand-dot"></span>
      <span class="brand-name">VELMORA</span>
    </div>
    <div class="front-details">
      <p class="person-name">Adrian Hale</p>
      <p class="person-title">Managing Director</p>
      <p class="address">12345, Address Goes Here<br>Country Name, 123456</p>
      <ul class="contact-list">
        <li>
          <svg class="contact-icon" viewBox="0 0 12 12"><path d="M2.5 0.5l2 2.5-1.2 1.3c.6 1.6 1.8 2.8 3.4 3.4L8 6.5l2.5 2-1 2.5C4.5 11 1 7.5 1 2.5z"/></svg>
          (044)-456-7890
        </li>
        <li>
          <svg class="contact-icon" viewBox="0 0 12 12"><path d="M3 0h6v12H3zM4 1.5v8h4v-8z"/></svg>
          123-456-7890
        </li>
        <li>
          <svg class="contact-icon" viewBox="0 0 12 12"><path d="M0 2h12v8H0zM1 3l5 3.5L11 3z" fill-rule="evenodd"/></svg>
          info@youremail.com
        </li>
        <li>
          <svg class="contact-icon" viewBox="0 0 12 12"><circle cx="6" cy="6" r="5.5"/></svg>
          www.website.com
        </li>
      </ul>
    </div>
  </section>
  <section class="card card-back">
    <span class="brand-dot"></span>
    <span class="brand-name">VELMORA</span>
  </section>
</main>
</body>
</html>
```